Billboard For Marek Delvaine

Need a Billboard 8ft. High x 16ft. Long. Ive attached a former billboard and looking for the same thing just updated with:
Summit Lodge Award Logo - 2020, 2022
Pinnacle Ring award Logo - 2022

Thanks.

```html
<!DOCTYPE html>
<html lang="en">
<head>
<meta charset="utf-8">
<title>Billboard – Marek Delvaine</title>
<link rel="stylesheet" href="https://fonts.googleapis.com/css2?family=Roboto:ital,wght@1,400&family=Lato:wght@400&family=Roboto+Condensed:wght@400;700&family=Jost:ital,wght@0,700;0,800;1,800&display=swap">
<style>
  :root {
    --page-bg: #d9dbda;
    --board-bg: #ffffff;
    --ink: #111111;
    --brand-red: #dc1433;
    --charcoal: #2e2d2f;
    --navy-strip: #3a5599;
    --shirt-blue: #3247a0;
    --skin-light: #efd9cf;
    --hair-grey: #8a8785;
  }
  html, body {
    margin: 0;
    width: 1200px;
    height: 1200px;
    overflow: hidden;
    background: var(--page-bg);
  }
  .billboard {
    position: absolute;
    left: 75px;
    top: 337px;
    width: 1050px;
    height: 525px;
    background: var(--board-bg);
    overflow: hidden;
  }
  .headline {
    position: absolute;
    left: 40px;
    top: 22px;
    margin: 0;
    font-family: "Roboto", sans-serif;
    font-style: italic;
    font-weight: 400;
    font-size: 90px;
    line-height: 80px;
    letter-spacing: 1px;
    color: var(--ink);
    white-space: nowrap;
  }
  .headline .call { color: var(--brand-red); }
  .contact-panel {
    position: absolute;
    left: 40px;
    top: 245px;
    width: 628px;
    height: 142px;
    background: var(--brand-red);
    border-radius: 12px;
  }
  .agent-name {
    position: absolute;
    left: 152px;
    top: 218px;
    width: 405px;
    height: 52px;
    background: var(--charcoal);
    border-radius: 7px;
    color: #fff;
    font-family: "Lato", sans-serif;
    font-size: 38px;
    line-height: 52px;
    text-align: center;
    letter-spacing: 1px;
    margin: 0;
    font-weight: 400;
    white-space: nowrap;
  }
  .agent-title {
    position: absolute;
    left: 40px;
    width: 628px;
    top: 280px;
    text-align: center;
    padding-right: 60px;
    box-sizing: border-box;
    font-family: "Roboto Condensed", sans-serif;
    font-size: 19px;
    color: var(--charcoal);
  }
  .agent-phone {
    position: absolute;
    left: 40px;
    width: 628px;
    top: 294px;
    text-align: center;
    font-family: "Jost", sans-serif;
    font-weight: 700;
    font-size: 80px;
    line-height: 92px;
    color: #fff;
    letter-spacing: 0;
    white-space: nowrap;
  }
  .tagline {
    position: absolute;
    left: 40px;
    width: 628px;
    top: 397px;
    text-align: center;
    font-family: "Jost", sans-serif;
    font-weight: 800;
    font-size: 22px;
    letter-spacing: 0.5px;
    color: var(--brand-red);
    white-space: nowrap;
  }
  .tagline em { font-style: italic; }
  .award {
    position: absolute;
    top: 452px;
    display: flex;
    align-items: center;
    gap: 8px;
    font-family: "Roboto Condensed", sans-serif;
    color: var(--ink);
    white-space: nowrap;
  }
  .award-seal { flex: none; }
  .award-text { line-height: 1; }
  .award-brand { font-size: 9px; letter-spacing: 0.5px; }
  .award-pinnacle { left: 153px; top: 456px; }
  .award-pinnacle .award-name { font-size: 17px; line-height: 17px; }
  .award-summit { left: 340px; }
  .award-summit .award-name { font-size: 15px; font-weight: 700; line-height: 15px; }
  .award-summit .award-note { font-size: 7px; margin-top: 2px; }
  .bottom-strip {
    position: absolute;
    left: 0;
    bottom: 0;
    width: 630px;
    height: 11px;
    background: var(--navy-strip);
  }
  .agent-portrait {
    position: absolute;
    left: 0;
    top: 0;
    width: 1050px;
    height: 525px;
  }
</style>
</head>
<body>
  <div class="billboard">
    <svg class="agent-portrait" viewBox="0 0 1050 525" role="img" aria-label="Portrait photo of the sales representative in a blue shirt and patterned tie, shown from the chest up">
      <defs>
        <linearGradient id="portraitTone" x1="0" y1="0" x2="0" y2="1">
          <stop offset="0" stop-color="var(--hair-grey)"/>
          <stop offset="0.2" stop-color="var(--skin-light)"/>
          <stop offset="0.68" stop-color="var(--skin-light)"/>
          <stop offset="0.8" stop-color="var(--shirt-blue)"/>
          <stop offset="1" stop-color="var(--shirt-blue)"/>
        </linearGradient>
      </defs>
      <path d="M785,60 Q800,15 880,15 Q960,15 975,80 L985,330 Q1050,380 1050,400 L1050,525 L627,525 Q660,440 735,400 Q790,370 790,330 Z" fill="url(#portraitTone)"/>
    </svg>

    <h1 class="headline">BUYING OR<br>SELLING? <span class="call">CALL</span></h1>

    <div class="contact-panel"></div>
    <h2 class="agent-name">MAREK DELVAINE</h2>
    <div class="agent-title">SALES REPRESENTATIVE.</div>
    <div class="agent-phone">613.555.0147</div>
    <div class="tagline">FOCUSED, DRIVEN AND <em>EXPERIENCED!</em></div>

    <div class="award award-pinnacle">
      <svg class="award-seal" width="36" height="36" viewBox="0 0 36 36"><circle cx="18" cy="18" r="17" fill="var(--ink)"/></svg>
      <div class="award-text">
        <div class="award-brand">HARBOR KEYSTONE</div>
        <div class="award-name">PINNACLE RING<br>AWARD 2022</div>
      </div>
    </div>

    <div class="award award-summit">
      <svg class="award-seal" width="54" height="54" viewBox="0 0 54 54"><circle cx="27" cy="27" r="26" fill="none" stroke="var(--ink)" stroke-width="1.5"/></svg>
      <div class="award-text">
        <div class="award-brand">HARBOR KEYSTONE</div>
        <div class="award-name">SUMMIT<br>LODGE</div>
        <div class="award-note">NATIONAL TOP 1% · 2020, 2022</div>
      </div>
    </div>

    <div class="bottom-strip"></div>
  </div>
</body>
</html>
```